Recreate a label for a champagne bottle [See attached example]

I'm needing to recreate a label for a champagne bottle label to give as closing gifts to clients when they purchase a home. Please include the following text "Welcome Home", my initials "R.T", "Established Year", the hashtag #BubbLORNE and my logo (attached). I prefer to have a black or white background with a crisp, easy to read cursive font similar to the Dunmore bourbon font. I want it to look as similar of a layout to the Valcorta label as possible

Target Market(s)

Luxury

Font styles to use
Decorative
Script

Colors

Designer to choose only greyscale colors for use in the design.

Requirements
Must have
• "Welcome Home", my initials "R.T", "Established Year", the hashtag #BubbLORNE and my logo
Nice to have
• Clean cursive font, easy to read, luxury look.
Should not have
• Clutter, too much design.

```html
<!DOCTYPE html>
<html lang="en">
<head>
<meta charset="utf-8">
<title>Welcome Home – Champagne Labels</title>
<link rel="stylesheet" href="https://fonts.googleapis.com/css2?family=Alex+Brush&family=Marcellus&family=Lato:wght@700;900&display=swap">
<style>
  :root {
    --gold-dark: #8a7636;
    --gold-mid: #b9a45c;
    --gold-light: #f4e8b8;
    --ink: #111111;
    --night: #1a1a1a;
    --paper: #ffffff;
    --mist: #e9e9e9;
    --page: #ffffff;
    --gold-gradient: linear-gradient(90deg, var(--gold-dark) 0%, var(--gold-light) 45%, var(--gold-mid) 70%, var(--gold-dark) 100%);
  }
  * { margin: 0; padding: 0; box-sizing: border-box; }
  html, body { width: 1200px; height: 1020px; overflow: hidden; background: var(--page); }
  .canvas {
    width: 1200px; height: 1020px;
    display: flex; align-items: center; justify-content: center; gap: 40px;
  }
  .label {
    position: relative; width: 540px; height: 540px;
    padding: 12px;
    background: var(--gold-gradient);
  }
  .label__field {
    position: relative; width: 100%; height: 100%; overflow: hidden;
  }
  .label--black .label__field { background: var(--ink); }
  .label--white .label__field { background: var(--paper); }
  .label__rays { position: absolute; inset: 0; }
  .label--black .label__rays { background: radial-gradient(circle at 50% 48%, #3a3a3a 0%, #1c1c1c 45%, #050505 100%); }
  .label--white .label__rays { background: radial-gradient(circle at 50% 48%, #ffffff 0%, #f1f1f1 50%, #e2e2e2 100%); }
  .label__rule {
    position: absolute; inset: 7px; border: 2px solid var(--gold-mid);
  }
  .label__pennant {
    position: absolute; top: 0; left: 50%; transform: translateX(-50%);
    width: 100px; height: 118px;
    background: linear-gradient(90deg, var(--gold-dark), var(--gold-light) 50%, var(--gold-mid));
    clip-path: polygon(0 0, 100% 0, 100% 86%, 50% 100%, 0 86%);
    display: flex; align-items: center; justify-content: center;
    padding-bottom: 14px;
  }
  .label__brand {
    font-family: "Lato", sans-serif; font-weight: 900; font-size: 15px;
    color: var(--paper); letter-spacing: 0.5px;
  }
  .label__oval { position: absolute; left: 50%; top: 183px; transform: translateX(-50%); }
  .label--white .label__oval ellipse.inner { fill: var(--mist); }
  .label--black .label__oval ellipse.inner { fill: var(--night); }
  .label__title {
    position: absolute; left: 0; right: 0; top: 222px; text-align: center;
    font-family: "Alex Brush", cursive; font-size: 80px; line-height: 1;
    background: linear-gradient(90deg, var(--gold-dark), var(--gold-light) 40%, var(--gold-mid) 65%, var(--gold-dark));
    -webkit-background-clip: text; background-clip: text; color: transparent;
  }
  .label__initials {
    position: absolute; left: 0; right: 0; top: 386px; text-align: center;
    font-family: "Marcellus", serif; font-size: 40px; font-weight: 700;
  }
  .label--black .label__initials { color: var(--paper); }
  .label--white .label__initials { color: var(--ink); }
  .label__hashtag {
    position: absolute; left: 50%; top: 436px; transform: translateX(-50%);
    width: 246px; height: 35px;
    background: linear-gradient(90deg, var(--gold-dark), var(--gold-mid) 40%, var(--gold-light) 60%, var(--gold-dark));
    font-family: "Lato", sans-serif; font-weight: 700; font-size: 23px;
    line-height: 35px; text-align: center;
  }
  .label--black .label__hashtag { color: var(--ink); }
  .label--white .label__hashtag { color: var(--paper); }
  .label__year {
    position: absolute; left: 0; right: 0; top: 482px; text-align: center;
    font-family: "Lato", sans-serif; font-weight: 700; font-size: 22px; letter-spacing: 4px;
  }
  .label--black .label__year { color: var(--paper); }
  .label--white .label__year { color: var(--ink); }
</style>
</head>
<body>
<main class="canvas">

  <section class="label label--black">
    <div class="label__field">
      <div class="label__rays" role="img" aria-label="Fine radiating sunburst rays on black"></div>
      <div class="label__rule"></div>
      <div class="label__pennant"><span class="label__brand">Harbrook</span></div>
      <svg class="label__oval" width="300" height="182" viewBox="0 0 300 182">
        <defs>
          <linearGradient id="ovalGoldA" x1="0" x2="1">
            <stop offset="0" stop-color="#8a7636"/><stop offset="0.5" stop-color="#f4e8b8"/><stop offset="1" stop-color="#8a7636"/>
          </linearGradient>
        </defs>
        <ellipse class="inner" cx="150" cy="91" rx="146" ry="87" stroke="url(#ovalGoldA)" stroke-width="3"/>
      </svg>
      <div class="label__title">Welcome Home</div>
      <div class="label__initials">R.T</div>
      <div class="label__hashtag">#BubbLORNE</div>
      <div class="label__year">2023</div>
    </div>
  </section>

  <section class="label label--white">
    <div class="label__field">
      <div class="label__rays" role="img" aria-label="Fine radiating sunburst rays on white"></div>
      <div class="label__rule"></div>
      <div class="label__pennant"><span class="label__brand">Harbrook</span></div>
      <svg class="label__oval" width="300" height="182" viewBox="0 0 300 182">
        <defs>
          <linearGradient id="ovalGoldB" x1="0" x2="1">
            <stop offset="0" stop-color="#8a7636"/><stop offset="0.5" stop-color="#e0cf8e"/><stop offset="1" stop-color="#8a7636"/>
          </linearGradient>
        </defs>
        <ellipse class="inner" cx="150" cy="91" rx="146" ry="87" stroke="url(#ovalGoldB)" stroke-width="3"/>
      </svg>
      <div class="label__title">Welcome Home</div>
      <div class="label__initials">R.T</div>
      <div class="label__hashtag">#BubbLORNE</div>
      <div class="label__year">2023</div>
    </div>
  </section>

</main>
</body>
</html>
```